Morvel & Morvel**

Liquid Magnesium (400 mg) 4 oz
Liquid Ionic B12 (1,000 mcg) 2 oz
Probiotic 55 Billion 30 CT
Liquid Potassium 99mg
Liquid Iodide 225mcg
Liquid Strontium 100 mg
Liquid Iron 22mg
Liquid Ionic Zinc (50 mg) 2 oz
Liquid Ionic Selenium (300 mcg) 2 oz
Lonic Boron 6 mg
Fulvic Acid 250 mg
Chromium 550 mcg
Ox Bile 500 mg
Vitamin D3 1000 IU
Liver Support 1000 IU
Tonify blood 1000 IU
Adrenal Support 1000 IU
Constipation 1000 IU

Target Market(s)

public

Industry/Entity Type

Health And Wellness

Font styles to use
Serif

Requirements
Must have
• color
Nice to have
• I would like to see the designer's views.
Should not have
• I don't have any

```html
<!DOCTYPE html>
<html lang="en">
<head>
<meta charset="utf-8">
<title>Morvel &amp; Morvel – Supplement Label</title>
<link rel="stylesheet" href="https://fonts.googleapis.com/css2?family=Lato:wght@300&family=Arimo:wght@400&display=swap">
<style>
  :root {
    --frame-red: #992744;
    --ink-violet: #2e2a6e;
    --lavender-soft: #c9cbe8;
    --lavender-mist: #eceef9;
    --tree-red: #e0382a;
    --tree-purple: #3d1d74;
    --table-grey: #dadada;
    --table-line: #b9b9b9;
    --table-text: #1d1d1d;
    --paper: #ffffff;
  }
  * { box-sizing: border-box; margin: 0; padding: 0; }
  html, body {
    width: 983px; height: 1200px; overflow: hidden; background: var(--paper);
  }
  .canvas { position: relative; width: 983px; height: 1200px; }

  .label {
    position: absolute; left: 31px; top: 140px; width: 929px; height: 537px;
    background: var(--frame-red);
  }
  .label-field {
    position: absolute; left: 14px; top: 16px; width: 906px; height: 506px;
    background: radial-gradient(ellipse at 30% 40%, var(--paper) 0%, var(--lavender-mist) 100%);
  }
  .texture-panel {
    position: absolute; left: 698px; top: 0; width: 208px; height: 506px;
    background: linear-gradient(160deg, var(--lavender-mist) 0%, var(--lavender-soft) 100%);
  }

  .placeholder { position: absolute; }
  .crystal-arc {
    left: 54px; top: 51px; width: 246px; height: 116px;
    border-radius: 123px 123px 0 0;
    background: radial-gradient(ellipse at 50% 100%, transparent 55%, rgba(80,82,170,.55) 60%, rgba(80,82,170,.15) 78%, transparent 82%);
  }
  .tree-main {
    left: 57px; top: 224px; width: 225px; height: 228px;
    border-radius: 45% 45% 6px 6px;
    background: linear-gradient(180deg, var(--tree-red) 0%, var(--tree-purple) 100%);
  }
  .tree-ground {
    position: absolute; left: 58px; top: 452px; width: 223px; height: 3px;
    background: var(--tree-purple);
  }
  .crystal-top { left: 402px; top: 19px; width: 40px; height: 43px; border-radius: 50%;
    background: radial-gradient(circle, rgba(60,62,160,.75), rgba(60,62,160,0) 72%); }
  .crystal-bottom { left: 399px; top: 447px; width: 54px; height: 48px; border-radius: 50%;
    background: radial-gradient(circle, rgba(60,62,160,.75), rgba(60,62,160,0) 72%); }
  .crystal-cluster { left: 753px; top: 356px; width: 142px; height: 139px; border-radius: 50%;
    background: radial-gradient(circle, rgba(50,52,150,.8), rgba(50,52,150,0) 70%); }

  .brand-title {
    position: absolute; left: 28px; top: 176px; width: 300px;
    font-family: "Lato", sans-serif; font-weight: 300; font-size: 32px;
    letter-spacing: 1.5px; color: var(--ink-violet); white-space: nowrap;
  }
  .brand-spine {
    position: absolute; left: 409px; top: 68px; height: 370px;
    writing-mode: vertical-rl;
    font-family: "Lato", sans-serif; font-weight: 300; font-size: 44px;
    letter-spacing: 1px; color: var(--ink-violet); white-space: nowrap; line-height: 1;
  }

  .tree-badge-box {
    position: absolute; left: 569px; top: 28px; width: 116px; height: 125px; background: var(--paper);
  }
  .tree-badge {
    left: 569px; top: 28px; width: 111px; height: 113px;
    border-radius: 45% 45% 4px 4px;
    background: linear-gradient(180deg, var(--tree-red) 0%, var(--tree-purple) 100%);
  }
  .tree-badge-ground {
    position: absolute; left: 569px; top: 141px; width: 111px; height: 2px; background: var(--tree-purple);
  }

  .nutrient-table {
    position: absolute; left: 562px; top: 152px; width: 166px;
    border-collapse: collapse;
    font-family: "Arimo", Arial, sans-serif; font-size: 8px; color: var(--table-text);
  }
  .nutrient-table thead th { height: 13px; background: #c4c4c4; }
  .nutrient-table td {
    height: 16.5px; padding: 0 3px; border-bottom: 1px solid var(--table-line); white-space: nowrap;
  }
  .nutrient-table .name { width: 85px; background: var(--table-grey); border-right: 1px solid #8a8a8a; }
  .nutrient-table .amount { background: var(--paper); }

  .mission-box {
    position: absolute; left: 746px; top: 164px; width: 154px; height: 176px;
    border: 2px solid var(--ink-violet);
  }
  .mission-heading {
    position: absolute; left: 4px; top: 4px; width: 144px; height: 10px;
    background: linear-gradient(90deg, rgba(46,42,110,.55), rgba(46,42,110,.35));
  }
</style>
</head>
<body>
<main class="canvas">
  <section class="label">
    <div class="label-field" role="img" aria-label="Soft white marble texture with lavender veins">
      <div class="texture-panel" role="img" aria-label="Lavender brushstroke texture"></div>

      <div class="placeholder crystal-arc" role="img" aria-label="Arch of violet quartz crystals"></div>
      <h1 class="brand-title">Morvel &amp; Morvel</h1>
      <div class="placeholder tree-main" role="img" aria-label="Tree silhouette in red to purple gradient"></div>
      <div class="tree-ground"></div>

      <div class="placeholder crystal-top" role="img" aria-label="Small violet crystal"></div>
      <p class="brand-spine">Morvel &amp; Morvel</p>
      <div class="placeholder crystal-bottom" role="img" aria-label="Small violet crystal"></div>

      <div class="tree-badge-box"></div>
      <div class="placeholder tree-badge" role="img" aria-label="Small tree silhouette in red to purple gradient"></div>
      <div class="tree-badge-ground"></div>

      <table class="nutrient-table">
        <thead><tr><th></th><th></th></tr></thead>
        <tbody>
          <tr><td class="name">Liquid Magnesium</td><td class="amount">(400 mg) 4 oz</td></tr>
          <tr><td class="name">Liquid Ionic B12</td><td class="amount">(1,000 mcg) 2 oz</td></tr>
          <tr><td class="name">Probiotic 55</td><td class="amount">Billion 30 CT</td></tr>
          <tr><td class="name">Liquid Potassium</td><td class="amount">99mg</td></tr>
          <tr><td class="name">Liquid Iodide</td><td class="amount">225mcg</td></tr>
          <tr><td class="name">Liquid Strontium</td><td class="amount">100 mg</td></tr>
          <tr><td class="name">Liquid Iron</td><td class="amount">22mg</td></tr>
          <tr><td class="name">Liquid Ionic Zinc</td><td class="amount">(50 mg) 2 oz</td></tr>
          <tr><td class="name">Liquid Ionic Selenium</td><td class="amount">(300 mcg) 2 oz</td></tr>
          <tr><td class="name">Lonic Boron</td><td class="amount">6 mg</td></tr>
          <tr><td class="name">Fulvic Acid</td><td class="amount">250 mg</td></tr>
          <tr><td class="name">Chromium</td><td class="amount">550 mcg</td></tr>
          <tr><td class="name">Ox Bile</td><td class="amount">500 mg</td></tr>
          <tr><td class="name">Vitamin D3</td><td class="amount">1000 IU</td></tr>
          <tr><td class="name">Liver Support</td><td class="amount">1000 IU</td></tr>
          <tr><td class="name">Tonify blood</td><td class="amount">1000 IU</td></tr>
          <tr><td class="name">Adrenal Support</td><td class="amount">1000 IU</td></tr>
          <tr><td class="name">Constipation</td><td class="amount">1000 IU</td></tr>
        </tbody>
      </table>

      <div class="mission-box">
        <div class="mission-heading" role="img" aria-label="Hand-lettered heading: morvel mission"></div>
      </div>

      <div class="placeholder crystal-cluster" role="img" aria-label="Cluster of violet quartz crystals"></div>
    </div>
  </section>
</main>
</body>
</html>
```